business card design for chiropractor
Sore Ring Milo
business card design for chiropractor - Medical
Creative Brief
Use same font as used in my logo
Dr. Milo Fenwick
Chiropractor
418 Brisbay Lane Suite 305 Wilmington DE 19806
Bramblecrashspine@mailvento.com
Ifyourbacksoresringmilo.com
I have uploaded three logo designs we would like multiple options
Appointment card preferred with check boxes for day and lines for date and time as well as patients name

```html
<!DOCTYPE html>
<html lang="en">
<head>
<meta charset="utf-8">
<title>Sore Ring Milo – Business & Appointment Card</title>
<link rel="stylesheet" href="https://fonts.googleapis.com/css2?family=Open+Sans:ital,wght@0,400;0,600;0,700;0,800;1,600&display=swap">
<style>
  :root {
    --brand-red: #c8161d;
    --ink-grey: #5a5a5a;
    --rule-grey: #9a9a9a;
    --box-navy: #2b2f7a;
    --card-white: #ffffff;
    --stage: #ecebea;
  }
  * { box-sizing: border-box; margin: 0; padding: 0; }
  html, body { width: 1200px; height: 799px; overflow: hidden; }
  body {
    background: var(--stage);
    font-family: "Open Sans", Arial, sans-serif;
    color: var(--ink-grey);
    position: relative;
  }
  .card {
    position: absolute;
    top: 251px;
    width: 520px;
    height: 297px;
    background: var(--card-white);
    box-shadow: 0 6px 18px rgba(0,0,0,0.12);
    overflow: hidden;
  }
  .card--front { left: 50px; }
  .card--back { left: 630px; }

  /* Front */
  .corner {
    position: absolute;
    width: 150px; height: 150px;
    border-radius: 50%;
    background: var(--brand-red);
  }
  .corner--top-left { left: -75px; top: -75px; }
  .corner--bottom-right { right: -75px; bottom: -75px; }
  .front-body {
    position: absolute;
    left: 0; right: 0; top: 58px;
    text-align: center;
  }
  .doctor-name {
    color: var(--brand-red);
    font-weight: 700;
    font-size: 21px;
    line-height: 1.1;
  }
  .doctor-role { font-size: 13px; margin-top: 2px; }
  .brand {
    display: inline-flex;
    align-items: center;
    gap: 8px;
    margin: 18px 0 16px;
  }
  .brand-dot {
    width: 14px; height: 14px;
    border-radius: 50%;
    background: var(--brand-red);
  }
  .brand-name {
    color: var(--brand-red);
    font-weight: 700;
    font-size: 17px;
    letter-spacing: 0.3px;
  }
  .contact { font-size: 12.5px; line-height: 1.45; }

  /* Back */
  .appt-title {
    position: absolute;
    left: 26px; top: 16px;
    color: var(--brand-red);
    font-style: italic;
    font-weight: 600;
    font-size: 19px;
  }
  .brand--back {
    position: absolute;
    right: 22px; top: 20px;
    margin: 0;
  }
  .brand--back .brand-name { font-size: 13px; }
  .brand--back .brand-dot { width: 10px; height: 10px; }
  .field {
    position: absolute;
    display: flex;
    align-items: flex-end;
    font-size: 12px;
    gap: 4px;
  }
  .field-line {
    flex: 1;
    border-bottom: 1px solid var(--rule-grey);
    height: 12px;
  }
  .days {
    position: absolute;
    left: 26px; right: 26px; top: 150px;
    display: flex;
    justify-content: space-between;
    font-size: 12px;
  }
  .day { display: flex; align-items: center; gap: 4px; }
  .day-box {
    width: 13px; height: 11px;
    border: 1.5px solid var(--box-navy);
  }
  .notice {
    position: absolute;
    left: 0; right: 0; top: 222px;
    background: var(--brand-red);
    color: var(--card-white);
    font-weight: 700;
    font-size: 11.5px;
    text-align: center;
    padding: 3px 0;
  }
  .back-footer {
    position: absolute;
    left: 0; right: 0; top: 250px;
    text-align: center;
    font-size: 12px;
    line-height: 1.4;
  }
</style>
</head>
<body>
  <section class="card card--front" aria-label="Business card">
    <div class="corner corner--top-left"></div>
    <div class="corner corner--bottom-right"></div>
    <div class="front-body">
      <h1 class="doctor-name">Dr. Milo Fenwick</h1>
      <p class="doctor-role">Chiropractor</p>
      <div class="brand">
        <span class="brand-dot"></span>
        <span class="brand-name">Sore Ring Milo</span>
      </div>
      <p class="contact">418 Brisbay Lane Suite 305 Wilmington DE 19806</p>
      <p class="contact">P. 302 555 0147 E: Bramblecrashspine@mailvento.com</p>
      <p class="contact">Ifyourbacksoresringmilo.com</p>
    </div>
  </section>

  <section class="card card--back" aria-label="Appointment card">
    <h2 class="appt-title">Appointment</h2>
    <div class="brand brand--back">
      <span class="brand-dot"></span>
      <span class="brand-name">Sore Ring Milo</span>
    </div>
    <div class="field" style="left:26px; right:26px; top:56px;"><span>Name:</span><span class="field-line"></span></div>
    <div class="field" style="left:26px; width:250px; top:84px;"><span>Date:</span><span class="field-line"></span></div>
    <div class="field" style="left:290px; right:26px; top:84px;"><span>Time:</span><span class="field-line"></span><span>a.m. / p.m.</span></div>
    <div class="field" style="left:26px; right:26px; top:116px;"><span>Note:</span><span class="field-line"></span></div>
    <div class="days">
      <span class="day">Sun <span class="day-box"></span></span>
      <span class="day">Mon <span class="day-box"></span></span>
      <span class="day">Tue <span class="day-box"></span></span>
      <span class="day">Wed <span class="day-box"></span></span>
      <span class="day">Thu <span class="day-box"></span></span>
      <span class="day">Fri <span class="day-box"></span></span>
      <span class="day">Sat <span class="day-box"></span></span>
    </div>
    <div class="field" style="left:26px; right:26px; top:192px;"><span class="field-line"></span></div>
    <p class="notice">Please notify us of a cancellation at least 24hr in advance to avoid a cancellation fee.</p>
    <div class="back-footer">
      <p>418 Brisbay Lane Suite 305 Wilmington DE 19806</p>
      <p>Ifyourbacksoresringmilo.com</p>
    </div>
  </section>
</body>
</html>
```